Wedding "Survival Kit" Bag label

I saw a "Wedding Week Survival Kit" that someone create via this site. They had the same design printed twice (facing opposite directions) on the front of the oversized card and then folded it to top off a bag filled with goodies for their guests. That is what I'm looking to go as well as need help with the design for the card. We are getting married in the Riviera Maya on August 2nd, 2015 and both love very modern designs. Our names are Meris Dolvane and Otto Flemmerik.

We would like the label to say something like "Wedding Survival Kit" and have some type of cool, abs tract logo that includes our first names, the location and maybe even the date. Feel free to visit our wedding website for inspiration: www.merisandotto.example

Industry/Entity Type

Wedding

Font styles to use
Other font styles liked:
• Chalkduster or anything fun

Requirements
Must have
• A fun flare to it!! Bright colors are encouraged!
Should not have
• Traditional boring fonts, or basic design

```html
<!DOCTYPE html>
<html lang="en">
<head>
<meta charset="utf-8">
<title>Meris and Otto – Wedding Survival Kit</title>
<link rel="stylesheet" href="https://fonts.googleapis.com/css2?family=Rye&family=Pinyon+Script&family=Berkshire+Swash&family=Zilla+Slab:wght@300&display=swap">
<style>
  :root{
    --navy:#1a2a6e;
    --sky:#2f7fd0;
    --orange:#ef6a25;
    --teal:#2ab8c9;
    --ink:#1c2f78;
    --white:#ffffff;
  }
  html,body{margin:0;padding:0;overflow:hidden;background:var(--white);}
  .label{
    position:relative;width:1200px;height:772px;overflow:hidden;
    background:var(--teal);
  }
  .sky-panel{
    position:absolute;left:0;top:0;width:1200px;height:440px;
    background:var(--navy);
  }
  .flourish-glow{
    position:absolute;left:80px;top:20px;width:1040px;height:400px;
    background:radial-gradient(ellipse at 50% 55%, rgba(47,127,208,.55) 0%, rgba(47,127,208,.18) 45%, rgba(26,42,110,0) 72%);
  }
  .couple-names{margin:0;position:absolute;left:0;top:0;width:1200px;height:440px;color:var(--white);font-weight:400;}
  .couple-names .name{
    position:absolute;top:124px;width:700px;height:168px;
    font-family:"Rye",serif;font-size:168px;line-height:168px;
    text-align:center;white-space:nowrap;
    transform:scale(0.66,1.3);transform-origin:50% 50%;
  }
  .couple-names .name.first{left:-17px;}   /* centre at x 333 */
  .couple-names .name.second{left:570px;}  /* centre at x 920 */
  .couple-names .joiner{
    position:absolute;left:550px;top:160px;width:200px;text-align:center;
    font-family:"Pinyon Script",cursive;font-size:86px;line-height:1;
  }
  .ribbon{position:absolute;left:0;top:436px;width:1200px;height:136px;}
  .ribbon-title{
    position:absolute;left:0;top:462px;width:1200px;height:96px;
    display:flex;align-items:center;justify-content:center;
    font-family:"Zilla Slab",serif;font-weight:300;font-size:88px;
    letter-spacing:1px;color:var(--white);margin:0;white-space:nowrap;
  }
  .bloom{
    position:absolute;border-radius:50%;
    background:radial-gradient(circle, #e8f6ff 0%, #4fb3ee 30%, #2a7fd4 60%, rgba(42,184,201,0) 72%);
  }
  .bloom.warm{
    background:radial-gradient(circle, #fff 0%, #f08b3c 32%, #e2336d 55%, rgba(42,184,201,0) 72%);
  }
  .details{position:absolute;left:0;top:572px;width:1200px;height:200px;}
  .details svg{position:absolute;left:0;top:0;}
  .details p{
    position:absolute;left:0;width:1200px;margin:0;text-align:center;
    font-family:"Berkshire Swash",cursive;color:var(--ink);white-space:nowrap;
  }
  .details .place{top:14px;font-size:62px;}
  .details .date{top:86px;font-size:68px;}
</style>
</head>
<body>
<main class="label">
  <section class="sky-panel">
    <div class="flourish-glow" role="img" aria-label="Blue swirling ribbons, bubbles, scroll ornaments and white paint spatter behind the names"></div>
    <h1 class="couple-names">
      <span class="name first">MERIS</span>
      <span class="joiner">and</span>
      <span class="name second">OTTO</span>
    </h1>
  </section>

  <svg class="ribbon" viewBox="0 0 1200 136" width="1200" height="136" aria-hidden="true">
    <rect x="0" y="0" width="1200" height="136" fill="#ffffff"/>
    <path fill="#ef6a25" d="
      M0 16
      q7.5 -10 15 0 t15 0 t15 0 t15 0 t15 0 t15 0 t15 0 t15 0 t15 0 t15 0
      t15 0 t15 0 t15 0 t15 0 t15 0 t15 0 t15 0 t15 0 t15 0 t15 0
      t15 0 t15 0 t15 0 t15 0 t15 0 t15 0 t15 0 t15 0 t15 0 t15 0
      t15 0 t15 0 t15 0 t15 0 t15 0 t15 0 t15 0 t15 0 t15 0 t15 0
      t15 0 t15 0 t15 0 t15 0 t15 0 t15 0 t15 0 t15 0 t15 0 t15 0
      t15 0 t15 0 t15 0 t15 0 t15 0 t15 0 t15 0 t15 0 t15 0 t15 0
      t15 0 t15 0 t15 0 t15 0 t15 0 t15 0 t15 0 t15 0 t15 0 t15 0
      t15 0 t15 0 t15 0 t15 0 t15 0 t15 0 t15 0 t15 0 t15 0 t15 0
      L1200 128 L0 128 Z"/>
  </svg>
  <h2 class="ribbon-title">WEDDING SURVIVAL KIT</h2>

  <div class="bloom warm" role="img" aria-label="Orange and pink star flower ornament" style="left:-70px;top:545px;width:200px;height:200px;"></div>
  <div class="bloom" role="img" aria-label="Blue star flower ornament" style="left:145px;top:580px;width:180px;height:180px;"></div>
  <div class="bloom" role="img" aria-label="Blue star flower ornament" style="left:860px;top:580px;width:180px;height:180px;"></div>
  <div class="bloom warm" role="img" aria-label="Orange and pink star flower ornament" style="left:1080px;top:545px;width:200px;height:200px;"></div>

  <section class="details">
    <svg width="1200" height="200" viewBox="0 0 1200 200" aria-hidden="true">
      <g stroke="#ffffff" stroke-width="2" fill="none">
        <line x1="408" y1="10" x2="590" y2="10"/>
        <circle cx="600" cy="10" r="8"/>
        <line x1="610" y1="10" x2="792" y2="10"/>
        <line x1="408" y1="168" x2="590" y2="168"/>
        <circle cx="600" cy="168" r="8"/>
        <line x1="610" y1="168" x2="792" y2="168"/>
      </g>
    </svg>
    <p class="place">Riviera Maya</p>
    <p class="date">August 2nd, 2015</p>
  </section>
</main>
</body>
</html>
```